Stationary design for real estate company in Trinidad and Tobago

Kestra Realty Ltd. , real estate company operating in Trinidad and Tobago, requires a sleek, modern and professional stationary package to wow our customers and potential new clients. we want to look sleek and professional; first impressions count in this business!
Business Address:
Level 1, Marlowe Point Tower
4C Seldon Grove Boulevard
Marlowe Point
Colwyn Pereira Highway
Port of Spain
Trinidad
Tel: + 1 868 555 0147
www.kestra-tt.com
info@kestra-tt.com

```html
<!DOCTYPE html>
<html lang="en">
<head>
<meta charset="utf-8">
<title>Kestra Realty – Business Card</title>
<link href="https://fonts.googleapis.com/css2?family=Roboto:wght@400;500;700&display=swap" rel="stylesheet">
<style>
  :root {
    --navy: #13305a;
    --gold: #b99a5c;
    --gold-light: #cbb07a;
    --paper: #f7f7f8;
    --backdrop: #e6e6e7;
    --white: #ffffff;
  }
  * { box-sizing: border-box; margin: 0; padding: 0; }
  html, body {
    width: 1200px; height: 1200px; overflow: hidden;
    background: var(--backdrop);
    font-family: "Roboto", Arial, sans-serif;
  }
  .stage { position: relative; width: 1200px; height: 1200px; }
  .card {
    position: absolute; left: 262px; width: 686px; height: 392px;
    border-radius: 22px; overflow: hidden; background: var(--paper);
  }
  .card--front { top: 165px; }
  .card--back { top: 653px; }
  .card__wave { position: absolute; inset: 0; width: 100%; height: 100%; }

  .brand { position: absolute; display: flex; align-items: center; color: var(--navy); font-weight: 500; }
  .brand__dot { border-radius: 50%; background: var(--gold); flex: none; }
  .brand__text { display: flex; flex-direction: column; align-items: center; line-height: 1; }
  .brand__name { letter-spacing: 0.02em; }
  .brand--small { left: 62px; top: 118px; gap: 10px; }
  .brand--small .brand__dot { width: 36px; height: 36px; }
  .brand--small .brand__name { font-size: 52px; }
  .brand--small .brand__sub { font-size: 12px; letter-spacing: 1.55em; margin-top: 8px; padding-left: 1.55em; }
  .brand--large { left: 50%; top: 140px; transform: translateX(-50%); gap: 16px; }
  .brand--large .brand__dot { width: 58px; height: 58px; }
  .brand--large .brand__name { font-size: 84px; }
  .brand--large .brand__sub { font-size: 18px; letter-spacing: 2.45em; margin-top: 14px; padding-left: 2.45em; }

  .details {
    position: absolute; right: 38px; top: 110px; text-align: right; color: var(--white);
    font-size: 17px; line-height: 21.5px;
  }
  .details__name { color: var(--gold-light); font-weight: 700; font-size: 26px; line-height: 30px; }
  .details__title { font-size: 17px; }
  .details__address { margin-top: 19px; }
  .details__address + .details__address { margin-top: 17px; }

  .contact {
    position: absolute; right: 38px; top: 345px; display: flex; align-items: center; gap: 12px;
    color: var(--white); font-size: 17px;
  }
  .contact__item { display: flex; align-items: center; gap: 7px; }
  .contact__icon { width: 14px; height: 14px; fill: var(--gold); }
</style>
</head>
<body>
<main class="stage">
  <section class="card card--front">
    <svg class="card__wave" viewBox="0 0 800 457" preserveAspectRatio="none" aria-hidden="true">
      <path fill="var(--gold)" d="M0 277 C 90 340, 170 375, 260 352 C 380 318, 470 150, 580 84 C 660 40, 740 28, 800 35 L800 457 L0 457 Z"/>
      <path fill="var(--navy)" stroke="var(--white)" stroke-width="3" d="M-5 317 C 80 360, 170 392, 260 368 C 380 330, 470 165, 580 103 C 660 62, 740 54, 805 62 L805 460 L-5 460 Z"/>
    </svg>

    <div class="brand brand--small">
      <span class="brand__dot"></span>
      <div class="brand__text">
        <span class="brand__name">KESTRA</span>
        <span class="brand__sub">REALTY</span>
      </div>
    </div>

    <div class="details">
      <p class="details__name">Daniel Whitford</p>
      <p class="details__title">President</p>
      <p class="details__address">Level 1, Marlowe Point Tower<br>4C Seldon Grove Boulevard<br>Marlowe Point</p>
      <p class="details__address">Colwyn Pereira Highway<br>Port of Spain<br>Trinidad</p>
    </div>

    <div class="contact">
      <span class="contact__item">
        <svg class="contact__icon" viewBox="0 0 24 24" aria-hidden="true"><path d="M6.6 10.8a15.1 15.1 0 0 0 6.6 6.6l2.2-2.2a1 1 0 0 1 1-.25 11.4 11.4 0 0 0 3.6.57 1 1 0 0 1 1 1V20a1 1 0 0 1-1 1A17 17 0 0 1 3 4a1 1 0 0 1 1-1h3.5a1 1 0 0 1 1 1c0 1.25.2 2.45.57 3.57a1 1 0 0 1-.25 1z"/></svg>
        + 1 868 555 0147
      </span>
      <span class="contact__item">
        <svg class="contact__icon" viewBox="0 0 24 24" aria-hidden="true"><path d="M2 5h20v14H2z M2 5l10 8 10-8" fill="var(--gold)" stroke="var(--navy)" stroke-width="1.5"/></svg>
        info@kestra-tt.com
      </span>
      <span class="contact__item">
        <svg class="contact__icon" viewBox="0 0 24 24" aria-hidden="true"><circle cx="12" cy="12" r="10"/><path d="M2 12h20M12 2c3 3 3 17 0 20M12 2c-3 3-3 17 0 20" fill="none" stroke="var(--navy)" stroke-width="1.5"/></svg>
        www.kestra-tt.com
      </span>
    </div>
  </section>

  <section class="card card--back">
    <div class="brand brand--large">
      <span class="brand__dot"></span>
      <div class="brand__text">
        <span class="brand__name">KESTRA</span>
        <span class="brand__sub">REALTY</span>
      </div>
    </div>
  </section>
</main>
</body>
</html>
```